Build a landing page to promote a service (dialler consultation and support).

We are a call centre consultation firm and we need a landing page to promote a service. The service is Morvexa dialler consultation and support.
If you do not know what Morvexa is, please do some quick "Zumbrel" research for more information.
The landing page will be promoted with a paid advertisement, so we want something that is simple, and explains exactly what service we offer.
There are two objectives for the landing page:
1) A "call to action" which directs the user to a contact page, including a form plus all of our contact details.
2) A form for them viewers to enter their details to get a "FREE" quote for their project. This form should be placed on the main page.
Notes:
The call to action will require the viewer to enter their name, email, phone number as well as a description of their request. There will also need to be a drop down menu for the type of quote. This menu should have the following options:
1) Morvexa support
2) Morvexa hosting
3) Morvexa customisation
4) Other
We need 2 pages in total:
1) Main landing page
This is the home page. It will need to clearly indicate our services and our key selling features.
Services:
* Morvexa support
* Morvexa hosting
* Morvexa customisation
Key Selling Features:
* Australian based
* PCI complaint
* 10+ years of dialler and call centre experience
* we run a sister company which is a highly reputable 40 seat call centre, so we know first hand about call centre technology.
The main landing page will have an "about us" section with a few paragraphs about how we got started.
-------------------------------------------------------------------------
2) Contact page
All of our contact details will live on this page, as well as a contact form.
Other notes:
We will be self hosting the landing page.
We already have a domain name.
The design must be clean and incorporate our logo, as well as it's colours. (Logo attached)
We want a fully function HTML landing page, not just a "PSD" design.
The page must be mobile optimised.
Anyone using Morvexa software.

```html
<!DOCTYPE html>
<html lang="en">
<head>
<meta charset="utf-8">
<title>Morvexa Support and Call Centre Technology</title>
<link rel="stylesheet" href="https://fonts.googleapis.com/css2?family=PT+Sans:wght@700&family=Lato:wght@400;700&display=swap">
<style>
  :root {
    --hero-deep: #2f5680;
    --hero-mid: #4a72a0;
    --hero-light: #7a9cc0;
    --text-white: #ffffff;
    --cta-coral: #e46a50;
  }
  * { margin: 0; padding: 0; box-sizing: border-box; }
  html, body { width: 735px; height: 1200px; overflow: hidden; }
  body { font-family: "Lato", sans-serif; background: var(--hero-deep); }
  .hero {
    position: relative;
    width: 735px;
    height: 1200px;
    overflow: hidden;
  }
  .hero-backdrop {
    position: absolute;
    inset: 0;
    background:
      radial-gradient(ellipse 340px 420px at 560px 420px, rgba(140,170,205,0.55), transparent 70%),
      radial-gradient(ellipse 300px 260px at 120px 80px, rgba(150,180,210,0.5), transparent 70%),
      linear-gradient(180deg, var(--hero-light) 0%, var(--hero-mid) 35%, var(--hero-deep) 75%, #24466c 100%);
  }
  .hero-content {
    position: relative;
    padding: 118px 60px 0 79px;
  }
  .hero-title {
    font-family: "PT Sans", sans-serif;
    font-weight: 700;
    font-size: 65px;
    line-height: 71px;
    color: var(--text-white);
    letter-spacing: -0.3px;
  }
  .hero-lead {
    margin-top: 54px;
    font-size: 33px;
    line-height: 45px;
    color: var(--text-white);
    max-width: 580px;
  }
  .quote-button {
    display: inline-flex;
    align-items: center;
    justify-content: center;
    margin-top: 97px;
    width: 490px;
    height: 100px;
    border-radius: 50px;
    background: var(--cta-coral);
    color: var(--text-white);
    font-weight: 700;
    font-size: 30px;
    letter-spacing: 0.5px;
    text-decoration: none;
  }
</style>
</head>
<body>
  <section class="hero">
    <div class="hero-backdrop" role="img" aria-label="Blue-tinted photo of a call centre agent wearing a headset working at computer monitors"></div>
    <div class="hero-content">
      <h1 class="hero-title">A holistic approach to Morvexa support and call centre technology</h1>
      <p class="hero-lead">A complete Morvexa call center consultation for better service, productivity and profitability.</p>
      <a class="quote-button" href="#quote">GET A FREE QUOTE</a>
    </div>
  </section>
</body>
</html>
```